bravokins mini muffin box packaging

I need two small boxes. Bravokins are mini muffins full of nutrition and protein. I will need a single small box for sampling and a little bigger box for 3 mini muffins . I would like to have this look really different yet functional and reasonable cost to make. Perhaps a space for each individual mini muffin. I will include my logo to be incorporated in someway with the packaging.
Need to see outside and inside of the boxes.

Target Market(s)

nutrition conscience people

Industry/Entity Type

Nutrition

Font styles to use
Serif

Colors
9bcb3c

Requirements
Must have
• bravokins name
• the dimensions are about 1 1/2 x 1 1/2 inches for each of the mini muffins
• green color as part
• box
• inside should craddle each of the mini muffins
• outside should in someway show the major concept: tasty and nutritious
Nice to have
• frog logo (as included in description)
• indications for each muffin in pack
Should not have
• sack like

```html
<!DOCTYPE html>
<html lang="en">
<head>
<meta charset="utf-8">
<title>Bravokins Mini Muffins – Box Lid</title>
<link rel="stylesheet" href="https://fonts.googleapis.com/css2?family=Baloo+2:wght@700;800&family=Arimo:wght@400;700&display=swap">
<style>
  :root {
    --lime: #9bcb3c;
    --lime-light: #b4dc52;
    --lime-dark: #86b82e;
    --forest: #2f6b2a;
    --forest-deep: #1f5a1f;
    --brown: #6b4a12;
    --brown-light: #8a6418;
    --cream: #f4efe4;
    --photo-warm: #e9d7b4;
    --photo-cocoa: #b69a7a;
    --white: #ffffff;
    --ground-top: #f3f3f3;
    --ground-bottom: #d9d9d9;
  }
  * { margin: 0; padding: 0; box-sizing: border-box; }
  html, body { width: 1200px; height: 1200px; overflow: hidden; }
  body {
    background: radial-gradient(ellipse at center, var(--ground-top) 0%, var(--ground-bottom) 100%);
    font-family: "Arimo", Arial, sans-serif;
    position: relative;
  }
  .box { position: absolute; left: 120px; top: 262px; width: 960px; }
  .lid { position: relative; width: 960px; height: 505px; }
  .lid-art { position: absolute; inset: 0; }
  .front {
    position: relative; height: 160px;
    background: linear-gradient(180deg, var(--lime-light) 0%, var(--lime) 60%, var(--lime-dark) 100%);
    border-top: 2px solid var(--lime-dark);
  }
  .brand-mark {
    position: absolute; display: flex; align-items: center; gap: 8px;
    font-family: "Baloo 2", sans-serif; font-weight: 800; font-size: 30px;
    color: var(--forest-deep);
  }
  .brand-mark .dot { width: 22px; height: 22px; border-radius: 50%; background: var(--forest-deep); }
  .lid .brand-mark { left: 22px; top: 40px; }
  .front .brand-mark { right: 24px; top: 56px; }
  .claims {
    position: absolute; right: 24px; top: 12px; display: flex; gap: 14px;
    font-size: 13px; line-height: 1.05; color: var(--white); text-align: center;
  }
  .title-block { position: absolute; left: 0; right: 0; top: 112px; text-align: center; }
  .brand-name {
    font-family: "Baloo 2", sans-serif; font-weight: 800; font-size: 40px; line-height: 1;
    color: var(--lime); letter-spacing: 0.5px;
    text-shadow: 0 0 4px var(--white), 0 0 4px var(--white), 0 0 4px var(--white);
  }
  .product-name {
    font-family: "Baloo 2", sans-serif; font-weight: 800; font-size: 104px; line-height: 1;
    color: var(--forest);
    -webkit-text-stroke: 0;
    text-shadow: 0 0 6px var(--white), 0 0 6px var(--white), 0 0 6px var(--white), 0 0 6px var(--white), 0 0 6px var(--white);
    margin-top: 4px;
  }
  .tagline {
    font-family: "Baloo 2", sans-serif; font-weight: 800; font-size: 40px; line-height: 1;
    color: var(--lime);
    text-shadow: 0 0 4px var(--white), 0 0 4px var(--white), 0 0 4px var(--white);
    margin-top: 6px;
  }
  .net-weight, .count {
    position: absolute; bottom: 24px;
    font-weight: 700; font-size: 21px; color: var(--white);
  }
  .net-weight { left: 22px; }
  .count { right: 22px; }
  .flavour {
    position: absolute; left: 40px; top: 20px;
    font-family: "Baloo 2", sans-serif; font-weight: 800; font-size: 58px; line-height: 0.82;
    color: var(--brown);
    text-shadow: 0 0 3px var(--cream), 0 0 3px var(--cream), 0 0 3px var(--cream);
  }
</style>
</head>
<body>
  <div class="box">
    <section class="lid">
      <svg class="lid-art" width="960" height="505" viewBox="0 0 960 505">
        <defs>
          <linearGradient id="bandGreen" x1="0" y1="0" x2="0" y2="1">
            <stop offset="0" stop-color="#b4dc52"/>
            <stop offset="1" stop-color="#8cc033"/>
          </linearGradient>
          <linearGradient id="bakedGoods" x1="0" y1="0" x2="1" y2="0.4">
            <stop offset="0" stop-color="#e6cfa6"/>
            <stop offset="0.35" stop-color="#efe3cb"/>
            <stop offset="0.6" stop-color="#d9c3a4"/>
            <stop offset="1" stop-color="#ecdcbf"/>
          </linearGradient>
        </defs>
        <rect width="960" height="505" fill="url(#bandGreen)"/>
        <path d="M0,120 C260,40 560,45 960,45 L960,345 C780,335 560,440 300,410 C180,398 80,380 0,370 Z"
              fill="url(#bakedGoods)" role="img" aria-label="Photograph of assorted mini muffins"/>
        <path d="M0,120 C260,40 560,45 960,45" fill="none" stroke="#6b4a12" stroke-width="5"/>
        <path d="M0,370 C80,380 180,398 300,410 C560,440 780,335 960,345" fill="none" stroke="#6b4a12" stroke-width="5"/>
      </svg>
      <div class="brand-mark"><span class="dot"></span>Bravokins</div>
      <div class="claims">
        <span>No<br>Artificial Colors</span>
        <span>Made with<br>Real Chocolate</span>
      </div>
      <div class="title-block">
        <div class="brand-name">BRAVOKINS</div>
        <div class="product-name">Mini Muffins</div>
        <div class="tagline">Full of nutrition and protein</div>
      </div>
      <div class="net-weight">Net WT. 30g</div>
      <div class="count">3 Muffins</div>
    </section>
    <section class="front">
      <div class="flavour">Chocolate<br>MUFFINS</div>
      <div class="brand-mark"><span class="dot"></span>Bravokins</div>
    </section>
  </div>
</body>
</html>
```